Business Card for a Mortgage Agent (myself)

I need a business card for my new job as Mortgage Agent. The Broker's logo is to be on the card as well as the brokerage License number. Not sure if to include a photo or not. Info to be on card.
Dante Roux
Mortgage Agent
Lic # M47105386
Cell: 905-614-2753
Email: danterouxk.ma@fennmail.com
Web: www.karlvostermortgages.com
TPW Brokerage Lic. # 73918

```html
<!DOCTYPE html>
<html lang="en">
<head>
<meta charset="utf-8">
<title>TPW Mortgage Agent Business Card</title>
<link rel="stylesheet" href="https://fonts.googleapis.com/css2?family=Montserrat:wght@400;500;600;700&display=swap">
<style>
  :root {
    --brand-blue: #0b4e8c;
    --brand-yellow: #fcce0a;
    --paper: #ffffff;
    --backdrop: #f2f2f4;
    --font-main: "Montserrat", Arial, sans-serif;
  }
  * { margin: 0; padding: 0; box-sizing: border-box; }
  html, body {
    width: 1200px;
    height: 1000px;
    overflow: hidden;
    background: var(--backdrop);
    font-family: var(--font-main);
  }
  .canvas {
    position: relative;
    width: 1200px;
    height: 1000px;
  }
  .card {
    position: absolute;
    width: 535px;
    height: 306px;
    overflow: hidden;
  }

  /* Front face */
  .card-front {
    left: 336px;
    top: 145px;
    background: var(--brand-blue);
  }
  .brand-lockup {
    position: absolute;
    left: 0;
    top: 0;
    width: 535px;
    display: flex;
    flex-direction: column;
    align-items: center;
  }
  .brand-mark {
    display: flex;
    align-items: center;
    gap: 18px;
    margin-top: 110px;
    margin-left: 40px;
  }
  .brand-square {
    width: 34px;
    height: 34px;
    background: var(--brand-yellow);
  }
  .brand-name {
    font-weight: 600;
    font-size: 34px;
    letter-spacing: 26px;
    color: var(--paper);
  }
  .brand-band {
    position: absolute;
    left: 108px;
    top: 210px;
    width: 334px;
    height: 33px;
  }
  .brand-band svg { position: absolute; inset: 0; }
  .brand-tagline {
    position: absolute;
    inset: 0;
    display: flex;
    align-items: center;
    justify-content: center;
    font-size: 15.5px;
    font-weight: 500;
    letter-spacing: 1.2px;
    color: var(--brand-blue);
  }

  /* Back face */
  .card-back {
    left: 341px;
    top: 508px;
    background: var(--paper);
  }
  .agent-info {
    position: absolute;
    left: 71px;
    top: 60px;
    color: var(--brand-blue);
  }
  .agent-name {
    font-size: 31px;
    font-weight: 700;
    letter-spacing: -0.3px;
    line-height: 1;
  }
  .agent-title {
    margin-top: 12px;
    font-size: 15px;
    font-weight: 400;
  }
  .agent-licence {
    margin-top: 8px;
    font-size: 15px;
    font-weight: 700;
    margin-left: 2px;
  }
  .agent-contact {
    list-style: none;
    margin-top: 28px;
    font-size: 12.5px;
    font-weight: 600;
  }
  .agent-contact li { margin-bottom: 11px; }

  .back-brand {
    position: absolute;
    left: 312px;
    top: 196px;
    display: flex;
    align-items: center;
    gap: 14px;
  }
  .back-brand .brand-square { width: 24px; height: 24px; }
  .back-brand .brand-name {
    font-size: 30px;
    letter-spacing: 30px;
    margin-right: -30px;
    color: var(--brand-blue);
  }
  .brokerage-licence {
    position: absolute;
    left: 312px;
    top: 246px;
    font-size: 11px;
    font-weight: 600;
    letter-spacing: 0.3px;
    color: var(--brand-blue);
  }
</style>
</head>
<body>
<main class="canvas">

  <section class="card card-front" aria-label="Card front">
    <div class="brand-lockup">
      <div class="brand-mark">
        <span class="brand-square"></span>
        <span class="brand-name">TPW</span>
      </div>
    </div>
    <div class="brand-band">
      <svg width="334" height="33" viewBox="0 0 334 33">
        <polygon points="12,0 334,0 322,33 0,33" fill="#ffffff"/>
      </svg>
      <span class="brand-tagline">TRUE PATH WEALTH</span>
    </div>
  </section>

  <section class="card card-back" aria-label="Card back">
    <div class="agent-info">
      <h1 class="agent-name">Dante Roux</h1>
      <p class="agent-title">Mortgage Agent</p>
      <p class="agent-licence">M47105386</p>
      <ul class="agent-contact">
        <li>905 614 2753</li>
        <li>danterouxk.ma@fennmail.com</li>
        <li>www.karlvostermortgages.com</li>
      </ul>
    </div>
    <div class="back-brand">
      <span class="brand-square"></span>
      <span class="brand-name">TPW</span>
    </div>
    <p class="brokerage-licence">Brokerage Lic. # 73918</p>
  </section>

</main>
</body>
</html>
```